File your income taxes and walk away with cash today. direct mailer campaign

We prepare income tax returns. Our slogan is Walk away with cash today! Our marketing edge above our competition is the fact that clients can get up to $5000 the day they file. We also offer notary, payroll, and bookkeeping services. We would like something with cash on the card as well. Quill Ledger Returns is the name of our company and this campaign is actually for a direct mailer to client prospects that make under 25k a year, who will be looking for help preparing their income tax documents but also be looking for cash the same day they file. Our office will begin handing out checks on January 2nd!

Target Market(s)

My target market for this particular piece is Blacks and Hispanics of lower income.

Industry/Entity Type

Finance And Accounting

Font styles to use
Serif
Script

Colors
a54499
b768aa
33a6d7
33b8a4
e667a6
e34197

Requirements
Must have
• Quill Ledger Returns should be written is some form of script, prefer colors of Purple & aqua or Pink and Turquoise. Some form of cash that looks as real as possible.
Nice to have
• Here is our contact info:
• 412 North Caldwell Hammond Parkway
• Dallas, TX 75148
• (281) 555-0374
• www.quillledgerreturns.example
Should not have
• No white people or body parts

```html
<!DOCTYPE html>
<html lang="en">
<head>
<meta charset="utf-8">
<title>Quill Ledger Returns – Direct Mailer</title>
<link rel="stylesheet" href="https://fonts.googleapis.com/css2?family=Great+Vibes&family=Open+Sans:ital,wght@1,700;1,800&family=Kalam:wght@400&display=swap">
<style>
  :root {
    --teal: #33b8a4;
    --pink: #e34197;
    --pink-soft: #e667a6;
    --pink-pale: #f08cc3;
    --white: #ffffff;
    --photo-warm: #c0397f;
    --photo-deep: #3b2a3a;
  }
  html, body { margin: 0; padding: 0; width: 1200px; height: 696px; overflow: hidden; }
  body { background: var(--teal); font-family: "Open Sans", Arial, sans-serif; }
  .mailer { position: relative; width: 1200px; height: 696px; background: var(--teal); overflow: hidden; }

  .masthead { position: absolute; left: 0; top: 0; width: 680px; height: 118px; background: var(--white); }
  .brand-name {
    position: absolute; left: 40px; top: 16px; margin: 0; white-space: nowrap;
    font-family: "Great Vibes", cursive; font-weight: 400; font-size: 76px; line-height: 1;
    color: var(--pink);
  }
  .slogan-band { position: absolute; left: 0; top: 118px; width: 660px; height: 72px; background: var(--teal); }
  .slogan {
    position: absolute; left: 40px; top: 4px; margin: 0; white-space: nowrap;
    font-family: "Great Vibes", cursive; font-size: 56px; line-height: 1.1; color: var(--white); font-weight: 400;
  }

  .accent-block { position: absolute; left: 0; top: 330px; width: 566px; height: 270px; background: var(--pink); }
  .offer-box { position: absolute; left: 0; top: 190px; width: 544px; height: 384px; background: var(--white); }

  .perks { list-style: none; margin: 0; padding: 0; position: absolute; left: 30px; top: 16px; width: 486px; }
  .perks li {
    position: relative; padding-left: 22px; margin-bottom: 2px;
    font-style: italic; font-weight: 700; font-size: 26px; line-height: 1.24; color: var(--teal);
  }
  .perks li::before {
    content: ""; position: absolute; left: 0; top: 10px; width: 13px; height: 13px; border-radius: 50%;
    background: radial-gradient(circle at 35% 35%, #f7a8cf, var(--pink) 70%);
  }
  .extra-services {
    position: absolute; left: 10px; top: 250px; width: 520px; margin: 0; text-align: center;
    font-style: italic; font-weight: 800; font-size: 31px; line-height: 1.26; color: var(--pink);
  }

  .contact { position: absolute; left: 34px; top: 612px; color: var(--white); font-style: italic; font-weight: 700; font-size: 20px; line-height: 1.45; }
  .contact-line { display: flex; align-items: center; gap: 8px; white-space: nowrap; }
  .contact-line svg { width: 16px; height: 16px; flex: none; }
  .contact-gap { width: 14px; }

  .profile-frame { position: absolute; left: 790px; top: 90px; width: 410px; height: 606px; background: var(--pink); }
  .profile-strip { position: absolute; left: 680px; top: 400px; width: 150px; height: 296px; background: var(--pink-pale); }
  .profile-photo {
    position: absolute; left: 830px; top: 104px; width: 370px; height: 296px;
    background: linear-gradient(100deg, var(--photo-warm) 0%, #8a3a6a 40%, var(--photo-deep) 100%);
  }
  .profile-card { position: absolute; left: 830px; top: 400px; width: 370px; height: 296px; background: var(--white); }
  .profile-name { position: absolute; left: 34px; top: 10px; margin: 0; font-family: "Kalam", cursive; font-size: 30px; color: var(--teal); font-weight: 400; white-space: nowrap; }
  .profile-role { position: absolute; left: 34px; top: 50px; margin: 0; font-family: "Kalam", cursive; font-size: 19px; color: var(--teal); white-space: nowrap; }
  .clock-art {
    position: absolute; left: 16px; top: 90px; width: 354px; height: 206px;
    background: radial-gradient(ellipse at 50% 100%, #ffffff 0%, #f1f1f1 60%, #dcdcdc 100%);
  }
</style>
</head>
<body>
  <main class="mailer">
    <header class="masthead">
      <h1 class="brand-name">Quill Ledger Returns</h1>
    </header>
    <div class="slogan-band">
      <p class="slogan">Walk away with cash today !</p>
    </div>

    <div class="accent-block"></div>
    <section class="offer-box">
      <ul class="perks">
        <li>Up to $5000 Same day you file!</li>
        <li>We will get your maximum refund!</li>
        <li>Submit documents securely from your home!</li>
        <li>Our office will begin handing out checks on January 2nd!</li>
      </ul>
      <p class="extra-services">We also offer<br>Notary, Payroll,<br>Bookkeeping Services.</p>
    </section>

    <footer class="contact">
      <div class="contact-line">
        <svg viewBox="0 0 16 16"><circle cx="8" cy="8" r="7.2" fill="none" stroke="#fff" stroke-width="1.2"/><path d="M8 3.5a2.6 2.6 0 0 0-2.6 2.6C5.4 8 8 11.8 8 11.8s2.6-3.8 2.6-5.7A2.6 2.6 0 0 0 8 3.5z" fill="#fff"/><circle cx="8" cy="6.1" r="1" fill="#33b8a4"/></svg>
        <span>412 North Caldwell Hammond Parkway Dallas, TX 75148</span>
      </div>
      <div class="contact-line">
        <svg viewBox="0 0 16 16"><circle cx="8" cy="8" r="7.2" fill="none" stroke="#fff" stroke-width="1.2"/><path d="M5.4 4.2l1.4 1.6-.8 1.1c.5 1.1 1.3 1.9 2.4 2.4l1.1-.8 1.6 1.4-.9 1.3c-2.9-.3-5.2-2.6-5.5-5.5z" fill="#fff"/></svg>
        <span>(281) 555-0374</span>
        <span class="contact-gap"></span>
        <svg viewBox="0 0 16 16"><circle cx="8" cy="8" r="7.2" fill="none" stroke="#fff" stroke-width="1.2"/><rect x="4" y="5.2" width="8" height="5.6" rx="0.6" fill="#fff"/><path d="M4.3 5.6L8 8.4l3.7-2.8" fill="none" stroke="#33b8a4" stroke-width="0.9"/></svg>
        <span>www.quillledgerreturns.example</span>
      </div>
    </footer>

    <div class="profile-frame"></div>
    <div class="profile-strip"></div>
    <div class="profile-photo" role="img" aria-label="Portrait photo of the office manager and tax practitioner"></div>
    <aside class="profile-card">
      <p class="profile-name">Renata Okafor</p>
      <p class="profile-role">Manager, Tax Practitioner</p>
      <div class="clock-art" role="img" aria-label="Illustration of a clock face with a hand writing the words Time for Taxes"></div>
    </aside>
  </main>
</body>
</html>
```